Forward Thinking Civil Engineering Company Brochure

Objective: Create a visually compelling marketing folder that effectively communicates the company’s commitment to technical excellence, quality control, responsiveness, and sustainability. Design cascading card inserts for more details on each service area.

Use: The folder will be used for client meetings, proposals, and trade shows to present services, capabilities, and case studies in a structured and engaging manner. Front, back, and pockets may be used for design but one pocket should have location for business card.

Company Identity: Modern, innovative, and sustainability-focused.
Color Scheme/Typography: Align with our brand (see attached... the neutral color can be adjusted)
Style: Clean, professional, and forward-thinking perhaps with subtle technical elements (blueprints, grids, engineering icons).

Folder Size: Standard 9” x 12” presentation folder with pockets.
Branding Elements: Must include certifications (see www.q7vtrx.com homepage for the certifications...HUB, SBA etc)
Logo placement (front cover and inside pocket).

q7vtrx.com is old website do not pull branding concepts

Cascading Design: Insert cards should be stacked inside the folder, with visible section titles when inserted.
Left Pocket – 4 Cascading Cards (About Q7V, PS&E, Geotechnical Engineering, Construction Material Testing)
Largest: 8.75" x 11.5"
Medium-Large: 8.75" x 10.75"
Medium: 8.75" x 10"
Smallest: 8.75" x 9.25"
Right Pocket – 4 Cascading Cards (Construction, Engineering & Testing, Construction Management, Environmental Engineering, Drone and GIS Services)
Largest: 8.75" x 11.5"
Medium: 8.75" x 10"
Smallest: 8.75" x 9.25"

```html
<!DOCTYPE html>
<html lang="en">
<head>
<meta charset="utf-8">
<title>Q7V Engineering – Presentation Folder</title>
<link rel="stylesheet" href="https://fonts.googleapis.com/css2?family=Montserrat:wght@400;500;600;700&display=swap">
<style>
  :root{
    --stage:#e4e4e4;
    --paper:#ffffff;
    --sand-dark:#cfc7bc;
    --sand-light:#f1ede8;
    --orange:#c2561d;
    --ink:#4a4a4a;
    --ink-soft:#8a8a8a;
    --navy:#1f2a3a;
    --die:#8c8c8c;
  }
  *{box-sizing:border-box;margin:0;padding:0}
  html,body{width:1200px;height:3516px;overflow:hidden}
  body{background:var(--stage);font-family:"Montserrat",Arial,sans-serif;color:var(--ink);position:relative}
  .panel{position:absolute;width:460px;height:600px;background:var(--paper);overflow:hidden;box-shadow:0 0 0 1px rgba(0,0,0,.06)}
  .panel svg.art{position:absolute;inset:0;width:100%;height:100%}
  .brand{position:absolute;font-weight:600;color:var(--ink);letter-spacing:.02em;white-space:nowrap}
  .brand-lg{font-size:25px;left:150px;top:106px;width:290px;letter-spacing:0}
  .brand-sm{font-size:18px}
  .years-badge{position:absolute;right:10px;top:8px;width:50px;height:28px;background:var(--navy);color:#fff;font-size:10px;font-weight:700;display:flex;align-items:center;justify-content:center}
  .cover-copy{position:absolute;left:150px;top:360px;width:290px}
  .cover-title{font-size:19px;font-weight:500;line-height:1.2;color:var(--ink);letter-spacing:.03em}
  .cover-tagline{font-size:7px;color:var(--ink-soft);margin-top:4px}
  .services-title{font-size:17px;font-weight:600;color:var(--orange);margin-top:12px;letter-spacing:.03em}
  .services-list{list-style:none;display:grid;grid-template-columns:repeat(3,1fr);gap:3px 8px;margin-top:8px;font-size:6.5px;color:var(--ink)}
  .back-copy{position:absolute;left:30px;top:270px;width:300px}
  .back-label{font-size:8px;font-weight:600;color:var(--orange);margin:14px 0 6px}
  .cert-row{display:flex;gap:10px;flex-wrap:wrap;width:220px}
  .cert-badge{width:40px;height:20px;background:#c9ced6;border-radius:2px}
  .contact-row{display:flex;gap:20px;font-size:7px;color:var(--ink)}
  .pocket{position:absolute;left:0;bottom:0;width:460px;height:200px}
  .card-slot{position:absolute;width:110px;height:66px;border:1.5px solid var(--ink)}
  .dieline{position:absolute;left:0;width:1200px;height:190px}
</style>
</head>
<body>

<!-- Front cover -->
<section class="panel front-cover" style="left:370px;top:120px">
  <svg class="art" viewBox="0 0 460 600" preserveAspectRatio="none">
    <defs><linearGradient id="sand1" x1="0" y1="0" x2="0" y2="1"><stop offset="0" stop-color="#d6cfc5"/><stop offset="1" stop-color="#efebe6"/></linearGradient></defs>
    <path d="M0 0H460V300C330 270 180 240 0 270Z" fill="url(#sand1)"/>
    <rect x="120" y="170" width="340" height="110" fill="#e5dfd7" opacity=".7" role="img" aria-label="Faint city skyline silhouette"/>
    <path d="M0 70C90 30 200 10 300 38C200 25 100 50 0 100Z" fill="var(--orange)"/>
    <path d="M170 330C290 320 390 280 460 220V255C390 305 290 335 170 330Z" fill="var(--orange)"/>
  </svg>
  <div class="years-badge">15 YRS</div>
  <div class="brand brand-lg">Q7V ENGINEERING</div>
  <div class="cover-copy">
    <h1 class="cover-title">CIVIL ENGINEERING<br>CONSULTING FIRM</h1>
    <p class="cover-tagline">Applying innovative solutions to shape your future</p>
    <h2 class="services-title">SERVICES</h2>
    <ul class="services-list">
      <li>Roadway Design</li><li>Bridge Design</li><li>Drainage Design</li>
      <li>Structural Design</li><li>Geotechnical Services</li><li>Construction Management</li>
      <li>Material Testing</li><li>Traffic Engineering</li><li>Environmental Engineering</li>
      <li>Drone and GIS Services</li>
    </ul>
  </div>
</section>

<!-- Inside spread -->
<section class="panel inside-left" style="left:140px;top:980px">
  <svg class="art" viewBox="0 0 460 600" preserveAspectRatio="none">
    <path d="M0 0H460V250C300 200 150 190 0 230Z" fill="#e8e3dc"/>
    <rect x="0" y="60" width="460" height="400" fill="#f0f0f0" opacity=".8" role="img" aria-label="Faint blueprint floor plan"/>
    <path d="M0 40C120 10 240 0 460 20V30C250 15 120 30 0 70Z" fill="var(--orange)"/>
  </svg>
  <div class="pocket" style="background:#fff;border-top:1px solid #ddd">
    <div class="brand brand-sm" style="left:30px;top:60px">Q7V ENGINEERING</div>
  </div>
</section>
<section class="panel inside-right" style="left:600px;top:980px">
  <svg class="art" viewBox="0 0 460 600" preserveAspectRatio="none">
    <path d="M0 0H460V250C300 200 150 230 0 240Z" fill="#e8e3dc"/>
    <rect x="0" y="60" width="460" height="400" fill="#f0f0f0" opacity=".8" role="img" aria-label="Faint blueprint floor plan"/>
    <path d="M120 360C250 350 380 320 460 280V305C380 340 250 365 120 360Z" fill="var(--orange)"/>
  </svg>
  <div class="pocket" style="background:#fff;border-top:1px solid #ddd">
    <div class="card-slot" style="left:180px;top:60px"></div>
  </div>
</section>

<!-- Outer dieline: back + front -->
<section class="panel back-cover" style="left:140px;top:1780px">
  <svg class="art" viewBox="0 0 460 600" preserveAspectRatio="none">
    <path d="M0 0H460V230C300 200 150 170 0 200Z" fill="url(#sand1)"/>
    <path d="M0 60C90 25 200 10 300 30C200 20 100 45 0 90Z" fill="var(--orange)"/>
  </svg>
  <div class="back-copy">
    <div class="brand brand-sm" style="position:static">Q7V ENGINEERING</div>
    <p class="back-label">Certifications</p>
    <div class="cert-row"><span class="cert-badge"></span><span class="cert-badge"></span><span class="cert-badge"></span><span class="cert-badge"></span><span class="cert-badge"></span><span class="cert-badge"></span><span class="cert-badge"></span><span class="cert-badge"></span></div>
    <p class="back-label">Contact us</p>
    <div class="contact-row"><span>q7vtrx.com</span><span>1-555-010-0142</span></div>
  </div>
</section>
<section class="panel front-cover" style="left:600px;top:1780px">
  <svg class="art" viewBox="0 0 460 600" preserveAspectRatio="none">
    <path d="M0 0H460V300C330 270 180 240 0 270Z" fill="url(#sand1)"/>
    <rect x="120" y="170" width="340" height="110" fill="#e5dfd7" opacity=".7" role="img" aria-label="Faint city skyline silhouette"/>
    <path d="M0 70C90 30 200 10 300 38C200 25 100 50 0 100Z" fill="var(--orange)"/>
    <path d="M170 330C290 320 390 280 460 220V255C390 305 290 335 170 330Z" fill="var(--orange)"/>
  </svg>
  <div class="years-badge">15 YRS</div>
  <div class="brand brand-lg">Q7V ENGINEERING</div>
  <div class="cover-copy">
    <h1 class="cover-title">CIVIL ENGINEERING<br>CONSULTING FIRM</h1>
    <p class="cover-tagline">Applying innovative solutions to shape your future</p>
    <h2 class="services-title">SERVICES</h2>
    <ul class="services-list">
      <li>Roadway Design</li><li>Bridge Design</li><li>Drainage Design</li>
      <li>Structural Design</li><li>Geotechnical Services</li><li>Construction Management</li>
      <li>Material Testing</li><li>Traffic Engineering</li><li>Environmental Engineering</li>
      <li>Drone and GIS Services</li>
    </ul>
  </div>
</section>
<svg class="dieline" style="top:2380px" viewBox="0 0 1200 190">
  <g fill="#fff" stroke="var(--die)" stroke-width="1.5">
    <path d="M140 0V20H108V150H140V140Q140 180 180 180H560Q600 180 600 140V0Z"/>
    <path d="M600 0V140Q600 180 640 180H1020Q1060 180 1060 140V150H1092V20H1060V0Z"/>
  </g>
  <rect x="300" y="50" width="110" height="66" fill="none" stroke="var(--ink)" stroke-width="1.5"/>
  <text x="880" y="100" font-family="Montserrat, Arial, sans-serif" font-size="18" font-weight="600" fill="var(--orange)" text-anchor="middle" transform="rotate(180 880 94)">Q7V ENGINEERING</text>
</svg>

<!-- Inner dieline -->
<section class="panel inside-left" style="left:140px;top:2730px">
  <svg class="art" viewBox="0 0 460 600" preserveAspectRatio="none">
    <path d="M0 0H460V250C300 200 150 190 0 230Z" fill="#e8e3dc"/>
    <rect x="0" y="60" width="460" height="420" fill="#f0f0f0" opacity=".8" role="img" aria-label="Faint blueprint floor plan"/>
    <path d="M0 40C120 10 240 0 460 20V30C250 15 120 30 0 70Z" fill="var(--orange)"/>
  </svg>
</section>
<section class="panel inside-right" style="left:600px;top:2730px">
  <svg class="art" viewBox="0 0 460 600" preserveAspectRatio="none">
    <path d="M0 0H460V250C300 200 150 230 0 240Z" fill="#e8e3dc"/>
    <rect x="0" y="60" width="460" height="420" fill="#f0f0f0" opacity=".8" role="img" aria-label="Faint blueprint floor plan"/>
    <path d="M120 360C250 350 380 320 460 280V305C380 340 250 365 120 360Z" fill="var(--orange)"/>
  </svg>
</section>
<svg class="dieline" style="top:3330px" viewBox="0 0 1200 190">
  <g fill="#fff" stroke="var(--die)" stroke-width="1.5">
    <path d="M140 0V20H108V150H140V140Q140 180 180 180H560Q600 180 600 140V0Z"/>
    <path d="M600 0V140Q600 180 640 180H1020Q1060 180 1060 140V150H1092V20H1060V0Z"/>
  </g>
  <rect x="790" y="50" width="110" height="66" fill="none" stroke="var(--ink)" stroke-width="1.5"/>
</svg>

</body>
</html>
```